Quorvin 2025 Landing Page Image for www.quorvin-example.com

Hello please find the old landing page for a new startup called Quorvin. (www.quorvin-example.com) The company is in the sports area. We have a new logo for 2025 that is attached. We need a new landing page that says "Coming 2H 2025" Looking for something slightly different and exciting. Please find the new logo and old image attached.

Target Market(s)

Sports Media

Industry/Entity Type

Sports Media

Requirements
Must have
• Text: "Quorvin 2.0 Coming 2H 2025"

```html
<!DOCTYPE html>
<html lang="en">
<head>
<meta charset="UTF-8">
<title>Quorvin 2.0 – Coming 2H 2025</title>
<link rel="stylesheet" href="https://fonts.googleapis.com/css2?family=Orbitron:wght@500;700&display=swap">
<style>
  :root {
    --night: #0b0f14;
    --panel-top: #1d2833;
    --panel-bottom: #151c24;
    --sky: #10151b;
    --stand: #1a2026;
    --turf: #3f6a2a;
    --turf-dark: #24401b;
    --rail: #1f3566;
    --ink: #f2f5f8;
    --ink-soft: #d9e2ea;
    --glow: rgba(220, 235, 255, 0.55);
  }
  * { margin: 0; padding: 0; box-sizing: border-box; }
  html, body {
    width: 1200px;
    height: 675px;
    overflow: hidden;
    background: var(--night);
  }
  .banner {
    position: relative;
    width: 1200px;
    height: 675px;
    overflow: hidden;
    background: var(--night);
    font-family: "Orbitron", sans-serif;
    color: var(--ink);
  }
  .stadium-photo {
    position: absolute;
    left: 0;
    top: 0;
    width: 900px;
    height: 675px;
    background:
      radial-gradient(ellipse 70% 40% at 35% 72%, rgba(63,106,42,0.85), rgba(36,64,27,0.4) 60%, transparent 80%),
      linear-gradient(180deg, var(--sky) 0%, #161c22 30%, var(--stand) 50%, var(--turf-dark) 62%, var(--turf) 70%, var(--turf-dark) 78%, var(--rail) 84%, var(--night) 100%);
  }
  .side-panel {
    position: absolute;
    inset: 0;
    width: 1200px;
    height: 675px;
  }
  .version,
  .brand-name,
  .launch {
    position: absolute;
    white-space: nowrap;
    line-height: 1;
  }
  .version {
    left: 248px;
    top: 118px;
    font-size: 26px;
    font-weight: 500;
    letter-spacing: 2px;
    color: var(--ink-soft);
  }
  .brand-name {
    left: 105px;
    top: 160px;
    font-size: 112px;
    font-weight: 700;
    color: var(--ink);
    text-shadow: 0 0 18px var(--glow), 0 0 40px rgba(200, 225, 255, 0.35);
  }
  .launch {
    left: 105px;
    top: 364px;
    font-size: 40px;
    font-weight: 500;
    letter-spacing: 5px;
    color: var(--ink);
    text-shadow: 0 0 10px rgba(255,255,255,0.35);
  }
</style>
</head>
<body>
  <main class="banner">
    <div class="stadium-photo" role="img" aria-label="Night view of a floodlit football stadium with a green field and stands under a cloudy sky"></div>

    <svg class="side-panel" viewBox="0 0 1200 675" aria-hidden="true">
      <defs>
        <linearGradient id="panelFill" x1="0" y1="0" x2="0" y2="1">
          <stop offset="0" stop-color="#1d2833"/>
          <stop offset="1" stop-color="#151c24"/>
        </linearGradient>
        <linearGradient id="panelFade" x1="0" y1="0" x2="1" y2="0">
          <stop offset="0" stop-color="#0b0f14" stop-opacity="0"/>
          <stop offset="1" stop-color="#0b0f14" stop-opacity="0.6"/>
        </linearGradient>
      </defs>
      <rect x="560" y="0" width="640" height="675" fill="url(#panelFade)"/>
      <polygon points="775,0 1200,0 1200,675 615,675" fill="url(#panelFill)"/>
    </svg>

    <section class="headline">
      <span class="version">QUORVIN 2.0</span>
      <h1 class="brand-name">Quorvin</h1>
      <p class="launch">COMING 2H 2025</p>
    </section>
  </main>
</body>
</html>
```